New professional looking flyer for company

I need our flyer updated my flyer is the Lvb flyer Have attached current flyer so you know what services need to be listed. Want it to be in mainly dark colours like black and dark grey with pops of light grey, silver or white. i have added several photos for you to choose which ones work best with your design would like The photos to be in colour for the flyer. But can have a mix of greyscale if that works for your design j have attached another companies flyers as design ideas to show what I am looking for

Target Market(s)

new clients

Industry/Entity Type

transport and earthmoving

Colors

Designer to choose colors to be used in the design.

Requirements
Nice to have
• Look professional
Should not have
• No orange or red or green

```html
<!DOCTYPE html>
<html lang="en">
<head>
<meta charset="utf-8">
<title>Lvb Pty Ltd – Our Services</title>
<link rel="stylesheet" href="https://fonts.googleapis.com/css2?family=Roboto+Condensed:wght@400;700&display=swap">
<style>
  :root {
    --page: #c9c9c9;
    --ink: #0a0a0a;
    --band: #2a2a2a;
    --white: #ffffff;
    --silver: #d8d8d8;
    --frame: #9a9a9a;
    --photo-top: #7d9fc4;
    --photo-bottom: #9c9a96;
    --footer-tone: #4a4644;
  }
  html, body {
    margin: 0;
    width: 1199px;
    height: 1200px;
    overflow: hidden;
    background: var(--page);
    font-family: "Roboto Condensed", "Arial Narrow", sans-serif;
  }
  .flyer {
    position: absolute;
    left: 194px;
    top: 75px;
    width: 813px;
    height: 1052px;
    overflow: hidden;
    background:
      linear-gradient(180deg, var(--band) 0, #202020 210px, var(--ink) 212px, #151515 560px, var(--ink) 100%);
    box-shadow: 0 3px 8px rgba(0,0,0,.35);
    color: var(--white);
  }
  .brand {
    position: absolute;
    left: 60px;
    top: 122px;
    width: 290px;
    margin: 0;
    text-align: center;
    white-space: nowrap;
    font-weight: 700;
    font-size: 50px;
    line-height: 1;
    color: var(--silver);
    letter-spacing: 1px;
  }
  .hero-photo {
    position: absolute;
    left: 394px;
    top: -7px;
    width: 424px;
    height: 424px;
    border-radius: 50%;
    background: linear-gradient(180deg, var(--photo-top) 0%, var(--photo-bottom) 100%);
  }
  .hero-ring {
    position: absolute;
    left: 370px;
    top: -30px;
  }
  .title {
    position: absolute;
    left: 62px;
    top: 318px;
    width: 320px;
    margin: 0;
    text-align: center;
    font-weight: 700;
    font-size: 52px;
    line-height: 62px;
    text-transform: uppercase;
  }
  .services-frame {
    position: absolute;
    left: 26px;
    top: 470px;
  }
  .service {
    position: absolute;
    margin: 0;
    font-weight: 700;
    font-size: 22px;
    line-height: 30px;
    display: flex;
    align-items: flex-start;
    gap: 8px;
    white-space: nowrap;
  }
  .service svg { flex: none; margin-top: 8px; }
  .service-plain {
    position: absolute;
    left: 526px;
    top: 790px;
    margin: 0;
    font-size: 22px;
    font-weight: 400;
  }
  .col-left { left: 79px; }
  .col-right { left: 479px; }
  .footer-photo {
    position: absolute;
    left: 0;
    bottom: 0;
    width: 100%;
    height: 180px;
    background: linear-gradient(180deg, var(--ink) 0%, var(--footer-tone) 100%);
  }
  .closing {
    position: absolute;
    left: 0;
    top: 912px;
    width: 813px;
    margin: 0;
    text-align: center;
    font-size: 22px;
    line-height: 31px;
    color: var(--white);
  }
</style>
</head>
<body>
<main class="flyer">
  <p class="brand">Lvb Pty Ltd</p>

  <div class="hero-photo" role="img" aria-label="Excavator working on a dirt road build with traffic cones under a blue sky"></div>
  <svg class="hero-ring" width="480" height="480" viewBox="0 0 480 480" aria-hidden="true">
    <circle cx="236" cy="226" r="222" fill="none" stroke="var(--silver)" stroke-width="22" stroke-dasharray="60 8 120 14 40 6"/>
    <circle cx="236" cy="226" r="236" fill="none" stroke="var(--frame)" stroke-width="8" stroke-dasharray="30 20 80 12"/>
  </svg>

  <h1 class="title">Our<br>Services</h1>

  <svg class="services-frame" width="750" height="395" viewBox="0 0 750 395" aria-hidden="true">
    <rect x="10" y="10" width="730" height="370" rx="26" fill="rgba(0,0,0,.55)" stroke="var(--frame)" stroke-width="14" stroke-dasharray="140 6 60 4 200 8"/>
    <rect x="16" y="16" width="718" height="360" rx="22" fill="none" stroke="#6a6a6a" stroke-width="5" stroke-dasharray="40 30 90 20"/>
  </svg>

  <p class="service col-left" style="top:518px"><svg width="16" height="16" viewBox="0 0 16 16"><circle cx="8" cy="8" r="6.5" fill="none" stroke="var(--silver)" stroke-width="1.4"/><path d="M5 8.2l2 2 4-4" fill="none" stroke="var(--silver)" stroke-width="1.5"/></svg>Over size loads/Hot Shot Loads</p>
  <p class="service col-left" style="top:565px"><svg width="16" height="16" viewBox="0 0 16 16"><circle cx="8" cy="8" r="6.5" fill="none" stroke="var(--silver)" stroke-width="1.4"/><path d="M5 8.2l2 2 4-4" fill="none" stroke="var(--silver)" stroke-width="1.5"/></svg>Heavy Vehicle Recovery Services</p>
  <p class="service col-left" style="top:611px"><svg width="16" height="16" viewBox="0 0 16 16"><circle cx="8" cy="8" r="6.5" fill="none" stroke="var(--silver)" stroke-width="1.4"/><path d="M5 8.2l2 2 4-4" fill="none" stroke="var(--silver)" stroke-width="1.5"/></svg>Potable Water Deliveries</p>
  <p class="service col-left" style="top:657px"><svg width="16" height="16" viewBox="0 0 16 16"><circle cx="8" cy="8" r="6.5" fill="none" stroke="var(--silver)" stroke-width="1.4"/><path d="M5 8.2l2 2 4-4" fill="none" stroke="var(--silver)" stroke-width="1.5"/></svg>Road Building/Maintenance</p>
  <p class="service col-left" style="top:703px"><svg width="16" height="16" viewBox="0 0 16 16"><circle cx="8" cy="8" r="6.5" fill="none" stroke="var(--silver)" stroke-width="1.4"/><path d="M5 8.2l2 2 4-4" fill="none" stroke="var(--silver)" stroke-width="1.5"/></svg>Earthworks</p>
  <p class="service col-left" style="top:751px"><svg width="16" height="16" viewBox="0 0 16 16"><circle cx="8" cy="8" r="6.5" fill="none" stroke="var(--silver)" stroke-width="1.4"/><path d="M5 8.2l2 2 4-4" fill="none" stroke="var(--silver)" stroke-width="1.5"/></svg>Sand &amp; Metal Supply &amp; Cartage</p>

  <p class="service col-right" style="top:518px"><svg width="16" height="16" viewBox="0 0 16 16"><circle cx="8" cy="8" r="6.5" fill="none" stroke="var(--silver)" stroke-width="1.4"/><path d="M5 8.2l2 2 4-4" fill="none" stroke="var(--silver)" stroke-width="1.5"/></svg>Road Train Tippers</p>
  <p class="service col-right" style="top:565px"><svg width="16" height="16" viewBox="0 0 16 16"><circle cx="8" cy="8" r="6.5" fill="none" stroke="var(--silver)" stroke-width="1.4"/><path d="M5 8.2l2 2 4-4" fill="none" stroke="var(--silver)" stroke-width="1.5"/></svg>Road Train Tankers</p>
  <p class="service col-right" style="top:611px"><svg width="16" height="16" viewBox="0 0 16 16"><circle cx="8" cy="8" r="6.5" fill="none" stroke="var(--silver)" stroke-width="1.4"/><path d="M5 8.2l2 2 4-4" fill="none" stroke="var(--silver)" stroke-width="1.5"/></svg>Road Train Flat Tops</p>
  <p class="service col-right" style="top:657px"><svg width="16" height="16" viewBox="0 0 16 16"><circle cx="8" cy="8" r="6.5" fill="none" stroke="var(--silver)" stroke-width="1.4"/><path d="M5 8.2l2 2 4-4" fill="none" stroke="var(--silver)" stroke-width="1.5"/></svg>Drop Deck Trailers</p>
  <p class="service col-right" style="top:703px"><svg width="16" height="16" viewBox="0 0 16 16"><circle cx="8" cy="8" r="6.5" fill="none" stroke="var(--silver)" stroke-width="1.4"/><path d="M5 8.2l2 2 4-4" fill="none" stroke="var(--silver)" stroke-width="1.5"/></svg><span>Main Site accredited<br>equipment &amp; Operators</span></p>
  <p class="service-plain">Traffic Management</p>

  <div class="footer-photo" role="img" aria-label="Road train tanker on a dirt road at dusk"></div>
  <p class="closing">We offer a large range of services not listed so<br>Call us today for a personalised quote to suit your needs.</p>
</main>
</body>
</html>
```